Business Cards Design for the electrical wholesaler: clean bold dynamic :)

We need a business card design that would follow our latest brand guidelines. As an electrical wholesaler we want to bring a fresh look and feel into the industry. The design should be clean bold and dynamic. It should come alive with the renewed energy of our green colour. Our grey colour should keep things balanced and complement the notion of maturity and responsibility. We employ Lato as a corporate font however are not bound by this font and we’re open to interpretation here.

Target Market(s)

Electrical contractors

Industry/Entity Type

Business

Contact Information for Business Card

Logo
Name & Surname: Olena Dovbush
Job Title: Director of Marketing
Email: helen.dovbush@mailvane.example
Cell phone: XXX.XXX.XXXX
Address: 20917 - 87 Ave. Edmonton, AB, Canada. T6K 2R8
Business Phone: 780.555.0187
Website: www.qorvil.example

Font styles to use
Other font styles liked:
• Lato

Requirements
Must have
• Logo & website
Nice to have
• Brand elements - some of them you may find in the attached Brand Guidelines (e.g. three lines on the background signifying "W")

```html
<!DOCTYPE html>
<html lang="en">
<head>
<meta charset="utf-8">
<title>Qorvil business cards</title>
<link href="https://fonts.googleapis.com/css2?family=Lato:wght@400;700&display=swap" rel="stylesheet">
<style>
  :root {
    --page: #e9e9e7;
    --grey-light: #6b6e6f;
    --grey-dark: #2f3132;
    --green: #6cc334;
    --green-deep: #4fa51e;
    --green-bright: #8fd13f;
    --white: #ffffff;
    --icon: #e4571f;
    --font: "Lato", sans-serif;
  }
  * { box-sizing: border-box; margin: 0; padding: 0; }
  html, body { width: 1200px; height: 800px; overflow: hidden; }
  body {
    background: var(--page);
    font-family: var(--font);
    position: relative;
  }
  .card {
    position: absolute;
    width: 580px;
    height: 330px;
    left: 310px;
    border-radius: 22px;
    overflow: hidden;
    background: radial-gradient(ellipse at 65% 20%, var(--grey-light) 0%, #4a4d4e 45%, var(--grey-dark) 100%);
    box-shadow: 0 10px 24px rgba(0,0,0,.25);
  }
  .card-back { top: 45px; }
  .card-front { top: 420px; }

  .brand-name {
    position: absolute;
    font-family: var(--font);
    font-weight: 700;
    color: var(--white);
    letter-spacing: 1px;
    display: flex;
    align-items: center;
    gap: 12px;
  }
  .brand-mark {
    display: inline-block;
    background: var(--green);
    border-radius: 4px;
  }
  .card-back .brand-name { left: 60px; top: 80px; font-size: 58px; }
  .card-back .brand-mark { width: 30px; height: 30px; }

  .back-band {
    position: absolute;
    left: 0; right: 0; bottom: 0;
    height: 28px;
    background: linear-gradient(90deg, var(--green-deep), var(--green));
  }
  .address {
    position: absolute;
    right: 30px;
    bottom: 52px;
    color: var(--white);
    font-size: 15px;
    line-height: 1.35;
  }

  .front-band {
    position: absolute;
    left: 0; top: 0; bottom: 0;
    width: 36px;
    background: linear-gradient(180deg, var(--green-bright), var(--green-deep));
  }
  .card-front .brand-name { left: 90px; top: 100px; font-size: 52px; }
  .card-front .brand-mark { width: 26px; height: 26px; }

  .person {
    position: absolute;
    right: 50px;
    top: 122px;
    text-align: center;
    color: var(--white);
  }
  .person-name { font-size: 27px; font-weight: 700; }
  .person-role { font-size: 15px; margin-top: 2px; }

  .contacts {
    position: absolute;
    right: 40px;
    top: 200px;
    list-style: none;
    display: flex;
    flex-direction: column;
    gap: 9px;
  }
  .contact {
    width: 220px;
    height: 32px;
    background: linear-gradient(180deg, var(--green-bright), var(--green));
    border-radius: 16px 4px 16px 4px;
    display: flex;
    align-items: center;
    gap: 14px;
    padding-left: 16px;
    color: var(--white);
    font-size: 15px;
  }
  .contact svg { width: 16px; height: 16px; flex: none; }
</style>
</head>
<body>

<section class="card card-back">
  <div class="brand-name"><span class="brand-mark"></span>Qorvil</div>
  <p class="address">20917 - 87 Ave.<br>Edmonton, AB, Canada<br>T6K 2R8</p>
  <div class="back-band"></div>
</section>

<section class="card card-front">
  <div class="front-band"></div>
  <div class="brand-name"><span class="brand-mark"></span>Qorvil</div>
  <div class="person">
    <p class="person-name">Olena Dovbush</p>
    <p class="person-role">general director</p>
  </div>
  <ul class="contacts">
    <li class="contact">
      <svg viewBox="0 0 16 16" aria-hidden="true"><path fill="var(--icon)" d="M3.5 1.5l2.5 0 1 3.5-1.6 1.2a8 8 0 0 0 4.4 4.4L11 9l3.5 1v2.5c0 1-1 2-2 2C6.5 14.5 1.5 9.5 1.5 3.5c0-1 1-2 2-2z"/></svg>
      780.555.0187
    </li>
    <li class="contact">
      <svg viewBox="0 0 16 16" aria-hidden="true"><rect x="1" y="3.5" width="14" height="9" rx="1" fill="var(--icon)"/><path d="M1.5 4l6.5 5 6.5-5" fill="none" stroke="var(--green)" stroke-width="1.2"/></svg>
      hello@qorvil.example
    </li>
    <li class="contact">
      <svg viewBox="0 0 16 16" aria-hidden="true"><g fill="none" stroke="var(--icon)" stroke-width="1.4"><circle cx="8" cy="8" r="6.5"/><ellipse cx="8" cy="8" rx="2.8" ry="6.5"/><path d="M1.5 8h13M2.5 4.8h11M2.5 11.2h11"/></g></svg>
      www.qorvil.example
    </li>
  </ul>
</section>

</body>
</html>
```